Stationery Design Project

We are looking for a full revision of our existing stationary to include within this project:

- Letterhead
- Business card
- Compliment slip

The items should be a reflection of our new website which can be found at http://www.larkfieldchecks.co.uk/

Our logo files are included within the file brief

There are some further projects which we may approach the winning designer for as we need a revision to the front cover of our reports, a new price list and two brochures for specific target markets.

Industry/Entity Type

Business

```html
<!DOCTYPE html>
<html lang="en">
<head>
<meta charset="utf-8">
<title>Larkfield Checks — Stationery Set</title>
<link href="https://fonts.googleapis.com/css2?family=PT+Sans:ital,wght@0,400;0,700;1,400&display=swap" rel="stylesheet">
<style>
  :root {
    --backdrop-light: #8c8c8c;
    --backdrop-dark: #3a3a3a;
    --paper: #ffffff;
    --navy: #2e3170;
    --brand-ink: #3a3f82;
    --blue-deep: #2f3675;
    --blue-mid: #3450a0;
    --text-blue: #3b55a5;
    --rule: #3a3f82;
  }
  * { box-sizing: border-box; margin: 0; padding: 0; }
  html, body { width: 1200px; height: 886px; overflow: hidden; }
  body {
    position: relative;
    font-family: "PT Sans", Arial, sans-serif;
    background: radial-gradient(ellipse at 50% 50%, var(--backdrop-light) 0%, #666 55%, var(--backdrop-dark) 100%);
  }
  .sheet {
    position: absolute;
    background: var(--paper);
    overflow: hidden;
    box-shadow: 2px 3px 6px rgba(0,0,0,.45);
  }
  .sheet .wave { position: absolute; left: 0; top: 0; width: 100%; height: 100%; }

  .wordmark {
    position: absolute;
    color: var(--brand-ink);
    font-weight: 700;
    letter-spacing: .02em;
    text-transform: uppercase;
    white-space: nowrap;
    line-height: 1;
  }
  .wordmark--light { color: var(--paper); }

  .contact {
    position: absolute;
    list-style: none;
    color: var(--text-blue);
    border-left: 1px solid var(--rule);
    line-height: 1.1;
  }
  .contact li { display: flex; align-items: flex-start; }
  .contact .ic { flex: none; fill: var(--navy); }
  .contact--lg { font-size: 9.6px; padding-left: 6px; }
  .contact--lg li { margin-bottom: 1.6px; }
  .contact--lg .ic { width: 9px; height: 9px; margin: 1px 7px 0 0; }
  .contact--sm { font-size: 5.2px; padding-left: 3px; color: var(--paper); border-color: var(--paper); }
  .contact--sm li { margin-bottom: 1px; }
  .contact--sm .ic { width: 5px; height: 5px; margin: 0 3px 0 0; fill: var(--paper); }

  /* business card front */
  .card-front { left: 69px; top: 81px; width: 211px; height: 121px; }
  .card-front .wordmark { left: 30px; top: 40px; font-size: 13px; }
  .card-footer {
    position: absolute; left: 8px; right: 8px; bottom: 5px;
    display: flex; justify-content: space-between;
    font-size: 5.4px; color: var(--paper);
  }
  .card-footer span { display: flex; align-items: center; }
  .card-footer .ic { width: 5px; height: 5px; margin-right: 3px; fill: var(--paper); }

  /* business card back */
  .card-back { left: 302px; top: 81px; width: 212px; height: 121px; }
  .card-back .wordmark { right: 8px; top: 9px; font-size: 7.5px; }
  .holder { position: absolute; left: 16px; top: 30px; color: var(--paper); }
  .holder-name { font-size: 10px; }
  .holder-role { font-size: 6px; font-style: italic; text-align: right; }
  .card-back .contact { left: 116px; top: 33px; }

  /* envelope */
  .envelope { left: 19px; top: 247px; width: 577px; height: 250px; }
  .envelope .wordmark { left: 24px; top: 36px; font-size: 22px; }
  .envelope .contact { left: 427px; top: 19px; }

  /* compliment slip */
  .comp-slip { left: 23px; top: 550px; width: 574px; height: 250px; }
  .comp-slip .wordmark { left: 22px; top: 36px; font-size: 22px; }
  .comp-slip .contact { left: 425px; top: 16px; }
  .comp-title {
    position: absolute; right: 20px; top: 138px;
    font-family: Arial, "PT Sans", sans-serif;
    font-size: 19px; color: var(--text-blue);
  }

  /* letterhead */
  .letterhead { left: 637px; top: 126px; width: 513px; height: 665px; }
  .letterhead .wordmark { left: 10px; top: 36px; font-size: 18px; }
  .letterhead .contact { left: 364px; top: 14px; }
  .letterhead .wordmark--foot { left: auto; top: auto; right: 12px; bottom: 12px; font-size: 13px; }
</style>
</head>
<body>

<svg width="0" height="0" style="position:absolute" aria-hidden="true">
  <defs>
    <symbol id="i-home" viewBox="0 0 12 12"><path d="M0.5 6.2 6 1l5.5 5.2H10V11H7.3V8H4.7v3H2V6.2z"/></symbol>
    <symbol id="i-phone" viewBox="0 0 12 12"><path d="M2.2 1 4.4 .8l1 3-1.3 1c.8 1.6 1.8 2.6 3.1 3.2l1.1-1.3 2.9 1-.2 2.3C6.5 10.3 1.8 6.3 2.2 1z"/></symbol>
    <symbol id="i-fax" viewBox="0 0 12 12"><path d="M3.2 1h5.6v3.2H3.2zM1 5h10v5H1zm2.3 2.4v3.6h5.4V7.4z"/></symbol>
    <symbol id="i-mail" viewBox="0 0 12 12"><path d="M.5 2h11v8H.5zm1.2 1.2v.3L6 6.6l4.3-3.1v-.3zm0 1.7v4h8.6v-4L6 8z"/></symbol>
    <symbol id="i-web" viewBox="0 0 12 12"><path d="M6 .5a5.5 5.5 0 1 0 0 11A5.5 5.5 0 0 0 6 .5zm-1 1.4c-.8 1-1.4 2.2-1.3 3.6L1.8 5A4.3 4.3 0 0 1 5 1.9zm2 0A4.3 4.3 0 0 1 10.2 5L8.3 5.5C8.4 4.1 7.8 2.9 7 1.9zM1.8 7l1.9.5c.1 1.2.6 2 1.3 2.6A4.3 4.3 0 0 1 1.8 7zm8.4 0A4.3 4.3 0 0 1 7 10.1c.7-.6 1.2-1.4 1.3-2.6z"/></symbol>
    <linearGradient id="g-blue" x1="0" y1="0" x2="1" y2="0">
      <stop offset="0" stop-color="#2d3270"/>
      <stop offset=".45" stop-color="#3552a4"/>
      <stop offset="1" stop-color="#3450a0"/>
    </linearGradient>
    <linearGradient id="g-blue-rev" x1="0" y1="0" x2="1" y2="0">
      <stop offset="0" stop-color="#2f3d8a"/>
      <stop offset=".3" stop-color="#3552a4"/>
      <stop offset="1" stop-color="#2d3270"/>
    </linearGradient>
  </defs>
</svg>

<!-- Business card, front -->
<section class="sheet card-front" aria-label="Business card front">
  <svg class="wave" viewBox="0 0 211 121" preserveAspectRatio="none" aria-hidden="true">
    <path d="M0 104Q100 80 211 72V121H0z" fill="url(#g-blue)"/>
    <path d="M0 110Q100 87 211 78" fill="none" stroke="#fff" stroke-width=".8"/>
  </svg>
  <div class="wordmark">Larkfield Checks</div>
  <div class="card-footer">
    <span><svg class="ic"><use href="#i-mail"/></svg>info@larkfieldchecks.co.uk</span>
    <span><svg class="ic"><use href="#i-web"/></svg>www.larkfieldchecks.co.uk</span>
  </div>
</section>

<!-- Business card, back -->
<section class="sheet card-back" aria-label="Business card back">
  <svg class="wave" viewBox="0 0 212 121" preserveAspectRatio="none" aria-hidden="true">
    <path d="M0 0H212V106Q110 66 0 58z" fill="url(#g-blue)"/>
    <path d="M0 64Q110 72 212 112" fill="none" stroke="#3a3f82" stroke-width=".8"/>
  </svg>
  <div class="wordmark wordmark--light">Larkfield Checks</div>
  <div class="holder">
    <div class="holder-name">Daniel Marsh</div>
    <div class="holder-role">Director</div>
  </div>
  <ul class="contact contact--sm">
    <li><svg class="ic"><use href="#i-home"/></svg><span>48 Orchard Lane, Elmwood Vale<br>SA 5021</span></li>
    <li><svg class="ic"><use href="#i-phone"/></svg><span>1300 482 615</span></li>
    <li><svg class="ic"><use href="#i-phone"/></svg><span>1300 482 615</span></li>
    <li><svg class="ic"><use href="#i-fax"/></svg><span>1300 482 730</span></li>
  </ul>
</section>

<!-- Envelope -->
<section class="sheet envelope" aria-label="Envelope">
  <svg class="wave" viewBox="0 0 577 250" preserveAspectRatio="none" aria-hidden="true">
    <path d="M0 218Q260 148 577 128V250H0z" fill="url(#g-blue)"/>
    <path d="M0 228Q270 160 577 142" fill="none" stroke="#fff" stroke-width="2"/>
  </svg>
  <div class="wordmark">Larkfield Checks</div>
  <ul class="contact contact--lg">
    <li><svg class="ic"><use href="#i-home"/></svg><span>48 Orchard Lane, Elmwood Vale<br>SA 5021</span></li>
    <li><svg class="ic"><use href="#i-phone"/></svg><span>1300 482 615</span></li>
    <li><svg class="ic"><use href="#i-fax"/></svg><span>1300 482 730</span></li>
    <li><svg class="ic"><use href="#i-mail"/></svg><span>info@larkfieldchecks.co.uk</span></li>
    <li><svg class="ic"><use href="#i-web"/></svg><span>www.larkfieldchecks.co.uk</span></li>
  </ul>
</section>

<!-- Compliment slip -->
<section class="sheet comp-slip" aria-label="Compliment slip">
  <svg class="wave" viewBox="0 0 574 250" preserveAspectRatio="none" aria-hidden="true">
    <path d="M0 140Q300 150 574 228V250H0z" fill="url(#g-blue-rev)"/>
    <path d="M0 158Q300 168 574 238" fill="none" stroke="#fff" stroke-width="2"/>
  </svg>
  <div class="wordmark">Larkfield Checks</div>
  <ul class="contact contact--lg">
    <li><svg class="ic"><use href="#i-home"/></svg><span>48 Orchard Lane, Elmwood Vale<br>SA 5021</span></li>
    <li><svg class="ic"><use href="#i-phone"/></svg><span>1300 482 615</span></li>
    <li><svg class="ic"><use href="#i-fax"/></svg><span>1300 482 730</span></li>
    <li><svg class="ic"><use href="#i-mail"/></svg><span>info@larkfieldchecks.co.uk</span></li>
    <li><svg class="ic"><use href="#i-web"/></svg><span>www.larkfieldchecks.co.uk</span></li>
  </ul>
  <p class="comp-title">With Compliments</p>
</section>

<!-- Letterhead -->
<section class="sheet letterhead" aria-label="Letterhead">
  <svg class="wave" viewBox="0 0 513 665" preserveAspectRatio="none" aria-hidden="true">
    <path d="M0 597Q240 540 513 538V665H0z" fill="url(#g-blue)"/>
    <path d="M0 606Q250 552 513 552" fill="none" stroke="#fff" stroke-width="2"/>
  </svg>
  <div class="wordmark">Larkfield Checks</div>
  <ul class="contact contact--lg">
    <li><svg class="ic"><use href="#i-home"/></svg><span>48 Orchard Lane, Elmwood Vale<br>SA 5021</span></li>
    <li><svg class="ic"><use href="#i-phone"/></svg><span>1300 482 615</span></li>
    <li><svg class="ic"><use href="#i-fax"/></svg><span>1300 482 730</span></li>
    <li><svg class="ic"><use href="#i-mail"/></svg><span>info@larkfieldchecks.co.uk</span></li>
    <li><svg class="ic"><use href="#i-web"/></svg><span>www.larkfieldchecks.co.uk</span></li>
  </ul>
  <div class="wordmark wordmark--light wordmark--foot">Larkfield Checks</div>
</section>

</body>
</html>
```